Flyer-Design für bildenden Künstler
Die einzige Designerin, die es wirklich verstanden hat, mein ausführliches briefing in einem wunderschönen, eleganten und absolut einzigartigen Design umzusetzen. Die Zusammenarbeit war klasse, sie ist auf jede meiner Wünsche eingegangen und hat sie mit großer Geduld und Professionalität umgesetzt. Das hätte nicht besser laufen können. Bin begeistert, von ihrem künstlerischen Anspruch, dem feinen Sinn für Ästhetik und ihrer großen Kreativität.
Zielgruppe
Ich bin bildender Künstler, benötige einen außergewöhnlichen, sehr ästhetischen, einzigartigen, als Eyecatcher fungierenden, meine Kunst und Identität repräsentierenden Flyer zum Auslegen, um neue KundInnen zu gewinnen.
Aufgabenstellung
Er soll wenig Text beinhalten (ein Zitat, Anschrift und Kontaktmöglichkeiten, ein kleines statement zu meiner Kunstphilosophie), und Bilder meiner Kunst zeigen. Raum ist mir wichtig, genug Leerräume, damit ein in Szene gesetztes Zitat oder Foto meiner Kunstwerke gut wirken kann. Es soll Lust darauf machen, Anreiz bieten und Interesse wecken, auf meine homepage zu gehen. Die Einzigartigkeit meiner Kunst soll deutlich werden.
Die hochgelandenen Fotos zeigen meine Kunstwerke. Sie können als Hintergrundbild fungieren und dementsprechend auch die ganze Seite ausfüllen, sie können zugeschnitten werden und/oder mit Text überlagert sein. Manche Fotos (zum Beispiel die Kunstwerke mit Rahmen) eignen sich dagegen, sie auf einer ganzen Seite zu zeigen, ohne einen Text dazu. So eine Seite würde ich jedenfalls gerne dabei haben, wo ein Kunstwerk für sich alleine auf einer ganzen Seite dargestellt wird. 1O4A2598 oder 1O4A6076a bieten sich dafür an (diese und alle anderen Fotos sind zum Teil komprimiert und zugeschnitten; falls gewünscht bzw. die Qualität nicht gut ist, kann ich das Originalfoto senden, das unkomprimiert und nicht zugeschnitten ist. Auch kann die Helligkeit oder die Farbqualität verbessert werden, falls notwendig). Nicht alle Kunstbilder müssen verwendet werden.
Ich bin offen für jedes Flyerformat, tendiere zu einem ein 2 oder 3-seitigen Falzflyer hochkant oder im Querformat. Bin aber offen für Ideen und Vorschläge.
Die Texte unter der Datei 'Texte, Adresse, Zitate' enthalten einen kleinen Text, der verwendet werden soll. Unter 'Text für die Titelseite' ist ein Vorschlag für die Titelseite zu finden. Die Adresse muss vollständig erscheinen, und unter 'Zitate' sind mehrere meiner Zitate - auch davon soll eines verwendet werden.
BITTE AUSSCHLIEßLICH DIE FOTOS UND TEXTE VERWENDEN, DIE ICH HOCHGELADEN HABE, UND NICHTS VON MEINEN HOMEPAGES NEHMEN. DANKE!

```html
<!DOCTYPE html>
<html lang="de">
<head>
<meta charset="utf-8">
<title>Transformationen – Flyer</title>
<link rel="stylesheet" href="https://fonts.googleapis.com/css2?family=Jost:ital,wght@0,300;0,400;1,300&display=swap">
<style>
  :root {
    --backdrop: #f6d8e6;
    --paper: #fbfbf9;
    --mauve: #a57d92;
    --gold: #d9b48a;
    --art-deep: #8e5f74;
    --art-mid: #c28f9e;
    --art-warm: #d59a86;
    --art-haze: #e9dcdf;
  }
  * { margin: 0; padding: 0; box-sizing: border-box; }
  html, body { width: 1200px; height: 1200px; overflow: hidden; }
  body {
    background: var(--backdrop);
    font-family: "Jost", sans-serif;
    display: flex;
    align-items: center;
    justify-content: center;
  }
  .flyer-cover {
    position: relative;
    width: 1080px;
    height: 640px;
    background: var(--paper);
    overflow: hidden;
  }
  .artwork {
    position: absolute;
    left: 0;
    bottom: 0;
    width: 720px;
    height: 520px;
    background:
      radial-gradient(ellipse 55% 45% at 42% 70%, var(--art-warm) 0%, transparent 70%),
      radial-gradient(ellipse 40% 50% at 12% 60%, var(--art-deep) 0%, transparent 75%),
      radial-gradient(ellipse 90% 90% at 20% 85%, var(--art-mid) 0%, var(--art-haze) 60%, rgba(251,251,249,0) 100%);
    -webkit-mask-image: linear-gradient(to right, #000 45%, transparent 100%);
    mask-image: linear-gradient(to right, #000 45%, transparent 100%);
  }
  .artwork::after {
    content: "";
    position: absolute;
    inset: 0;
    background: linear-gradient(to bottom, var(--paper) 0%, rgba(251,251,249,0) 40%);
  }
  .brand {
    position: absolute;
    top: 70px;
    right: 80px;
    display: flex;
    align-items: center;
    gap: 10px;
    color: var(--gold);
    font-weight: 300;
    font-size: 15px;
    letter-spacing: 0.08em;
    text-transform: uppercase;
  }
  .brand-dot {
    width: 10px;
    height: 10px;
    border-radius: 50%;
    background: var(--gold);
  }
  .cover-text {
    position: absolute;
    right: 80px;
    bottom: 90px;
    text-align: right;
  }
  .quote {
    color: var(--gold);
    font-weight: 300;
    font-style: italic;
    font-size: 20px;
    line-height: 1.45;
    letter-spacing: 0.03em;
    margin-bottom: 44px;
  }
  .title {
    color: var(--mauve);
    font-weight: 300;
    font-size: 36px;
    letter-spacing: 0.32em;
    margin-right: -0.32em;
  }
</style>
</head>
<body>
  <article class="flyer-cover">
    <div class="artwork" role="img" aria-label="Nahaufnahme eines Kunstwerks mit rosafarbenen, korallenartigen Strukturen"></div>
    <div class="brand"><span class="brand-dot"></span>Jens Dornhaus · Art</div>
    <div class="cover-text">
      <p class="quote">„Die Suche nach der Wahrheit führt nur über<br>die Distanz zur Realität.“</p>
      <h1 class="title">TRANSFORMATIONEN</h1>
    </div>
  </article>
</body>
</html>
```